Quillet Studios business card

Front of card should be logo and back of card should be communication info.
Please note: reverse the logo color. Card should be black and everything else white.

Industry/Entity Type

Custom home design/construction

Contact Information for Business Card

Quillet Studios, LLC 555-382-0146 quilletstudios@mailbox-example.com

Requirements
Must have
• Square card, Logo on front, communication info on back and perhaps a mini version of the logo on back also. Black card/white lettering. Double sides square card.
Nice to have
• I want to keep it simple. Our product (custom homes) speak for themselves.

```html
<!DOCTYPE html>
<html lang="en">
<head>
<meta charset="utf-8">
<title>Quillet Studios business card</title>
<link rel="stylesheet" href="https://fonts.googleapis.com/css2?family=Montserrat:wght@400;500;600&display=swap">
<style>
  :root {
    --stage: #e9e4dc;
    --card: #000000;
    --ink: #ffffff;
    --rule: #9a9a9a;
  }
  * { box-sizing: border-box; margin: 0; padding: 0; }
  html, body {
    width: 1200px; height: 1200px; overflow: hidden;
    background: var(--stage);
    font-family: "Montserrat", sans-serif;
    color: var(--ink);
  }
  .canvas { position: relative; width: 1200px; height: 1200px; }
  .card {
    position: absolute;
    width: 520px; height: 520px;
    background: var(--card);
    box-shadow: 0 10px 28px rgba(0,0,0,.25);
  }
  .card--back { left: 100px; top: 70px; }
  .card--front { left: 580px; top: 610px; }

  .wordmark {
    position: absolute; left: 0; right: 0;
    text-align: center;
    font-weight: 600;
    text-transform: uppercase;
    color: var(--ink);
  }
  .card--back .wordmark {
    top: 150px; font-size: 30px; letter-spacing: 1px;
  }
  .card--front .wordmark {
    top: 235px; font-size: 44px; letter-spacing: 1px;
  }

  .contact-frame {
    position: absolute;
    left: 78px; top: 262px;
    width: 414px; height: 222px;
    border: 3px solid var(--ink);
    padding: 42px 40px 0 36px;
  }
  .contact-frame__name {
    font-size: 20px; font-weight: 600;
    letter-spacing: 3px; text-transform: uppercase;
    white-space: nowrap;
  }
  .contact-frame__rule {
    height: 1px; background: var(--rule);
    margin: 16px 0 20px;
  }
  .contact-line {
    display: flex; align-items: center; gap: 24px;
    font-size: 14px; font-weight: 500;
    margin: 0 0 10px 40px;
    white-space: nowrap;
  }
  .contact-line svg { width: 28px; height: 28px; flex: none; }
</style>
</head>
<body>
<main class="canvas">

  <section class="card card--back" aria-label="Back of card: contact information">
    <div class="wordmark">Quillet Studios</div>
    <div class="contact-frame">
      <div class="contact-frame__name">Quillet Studios, LLC</div>
      <div class="contact-frame__rule"></div>
      <div class="contact-line">
        <svg viewBox="0 0 28 28" aria-hidden="true">
          <circle cx="14" cy="14" r="14" fill="#fff"/>
          <path d="M10 7.5c.8-.5 1.5-.3 1.9.4l1.2 2.2c.3.6.2 1.2-.3 1.6l-.9.7c.6 1.6 1.8 3 3.4 3.8l.8-.9c.4-.5 1.1-.6 1.6-.3l2.2 1.3c.7.4.8 1.2.3 1.9l-.8 1c-.7.8-1.8 1.1-2.8.7-3.8-1.5-6.6-4.4-7.9-8.2-.3-1 0-2 .8-2.6z" fill="#000"/>
        </svg>
        <span>555-382-0146</span>
      </div>
      <div class="contact-line">
        <svg viewBox="0 0 28 28" aria-hidden="true">
          <circle cx="14" cy="14" r="14" fill="#fff"/>
          <rect x="7.5" y="9.5" width="13" height="9" fill="none" stroke="#000" stroke-width="1.4"/>
          <path d="M7.5 9.5l6.5 5 6.5-5M7.5 18.5l4.6-4.2M20.5 18.5l-4.6-4.2" fill="none" stroke="#000" stroke-width="1.2"/>
        </svg>
        <span>quilletstudios@mailbox-example.com</span>
      </div>
    </div>
  </section>

  <section class="card card--front" aria-label="Front of card: company name">
    <div class="wordmark">Quillet Studios</div>
  </section>

</main>
</body>
</html>
```